Business Card for Bright Meadow Lawn & Landscape

Double Sided Card Design - I think one side of the card should be cleaner, with logo, contact info, and "Complete Residential & Commercial Landscape Services", and on the other side it should list the services we offer:

- Lawn Care & Mowing
- Hedge & Shrub Trimming
- Leaf Removal & Clean Up
- Aeration & Sod
- Mulch & Rock Installations
- Landscape Installations & Renovations
- Commercial Snow Removal

Please make it clean and very professional... don't want it too be too busy, but want to tell them what we do.

Target Market(s)

Residential and Commercial

Industry/Entity Type

Landscape

Contact Information for Business Card

Fully Insured
Tobias Verhoek
410-555-2916
Tverhoek27@mailbrook.net

Requirements
Must have
• Double Sided, Cleaner on one side, more information and text on the other side.

```html
<!DOCTYPE html>
<html lang="en">
<head>
<meta charset="utf-8">
<title>Bright Meadow Lawn &amp; Landscape – Business Card</title>
<link href="https://fonts.googleapis.com/css2?family=Cinzel:wght@400;600&family=Lato:wght@400;700&display=swap" rel="stylesheet">
<style>
  :root {
    --charcoal: #48494b;
    --charcoal-deep: #3f4042;
    --leaf: #8cb521;
    --paper: #ffffff;
    --ink: #3a3a3c;
    --rule: #8d8e90;
    --backdrop: #e9eae6;
  }
  * { box-sizing: border-box; margin: 0; padding: 0; }
  html, body { width: 1200px; height: 900px; overflow: hidden; }
  body {
    background: var(--backdrop);
    font-family: "Lato", Arial, sans-serif;
    display: flex; flex-direction: column; align-items: center; justify-content: center;
    gap: 46px;
  }
  .card {
    position: relative; width: 660px; height: 377px; overflow: hidden;
    box-shadow: 0 10px 28px rgba(0,0,0,.18);
  }

  /* Services side */
  .card--services {
    background: var(--charcoal); color: var(--paper);
    text-align: center; padding: 34px 36px 30px;
    display: flex; flex-direction: column; justify-content: space-between;
  }
  .brand-title {
    font-family: "Cinzel", Georgia, serif; font-weight: 600;
    color: var(--leaf); font-size: 48px; line-height: 1; letter-spacing: 1px;
  }
  .brand-sub {
    font-family: "Cinzel", Georgia, serif; font-weight: 400;
    font-size: 21px; letter-spacing: 7px; margin-top: 6px; color: var(--paper);
  }
  .rule { height: 1px; background: var(--rule); margin: 0 14px; }
  .services {
    list-style: none; display: flex; flex-wrap: wrap; justify-content: center;
    gap: 6px 24px; font-size: 15.5px; line-height: 1.25; padding: 0 20px;
  }
  .tagline {
    font-family: "Cinzel", Georgia, serif; color: var(--leaf);
    font-size: 14px; letter-spacing: .6px; white-space: nowrap;
  }

  /* Contact side */
  .card--contact { background: var(--paper); }
  .card__swoosh { position: absolute; inset: 0; }
  .holder-name {
    position: absolute; left: 52px; top: 66px;
    font-family: "Cinzel", Georgia, serif; font-weight: 600;
    color: var(--leaf); font-size: 28px;
  }
  .brand-mark {
    position: absolute; right: 36px; top: 28px; width: 270px;
    display: flex; flex-direction: column; align-items: center; gap: 10px;
  }
  .brand-mark__dot { width: 50px; height: 50px; border-radius: 50%; background: var(--leaf); }
  .brand-mark__name {
    font-family: "Cinzel", Georgia, serif; font-weight: 600; color: var(--leaf);
    font-size: 22px; line-height: 1.15; text-align: center;
  }
  .contact-list {
    position: absolute; left: 52px; top: 196px; list-style: none;
    color: var(--ink); font-size: 18px; display: grid; gap: 6px;
  }
  .contact-list li { display: flex; align-items: center; gap: 9px; }
  .contact-list svg { width: 16px; height: 16px; fill: var(--leaf); }
  .insured {
    position: absolute; right: 40px; top: 268px;
    font-family: "Cinzel", Georgia, serif; color: var(--leaf);
    font-size: 22px; letter-spacing: 1px;
  }
</style>
</head>
<body>

<section class="card card--services">
  <div>
    <h1 class="brand-title">Bright Meadow</h1>
    <p class="brand-sub">LAWN &amp; LANDSCAPE</p>
  </div>
  <div class="rule"></div>
  <ul class="services">
    <li>Lawn Care &amp; Mowing</li>
    <li>Hedge &amp; Shrub Trimming</li>
    <li>Leaf Removal &amp; Clean Up</li>
    <li>Aeration &amp; Sod</li>
    <li>Mulch &amp; Rock Installations</li>
    <li>Landscape Installations &amp; Renovations</li>
    <li>Commercial Snow Removal</li>
  </ul>
  <div class="rule"></div>
  <p class="tagline">Complete Residential &amp; Commercial Landscape Services</p>
</section>

<section class="card card--contact">
  <svg class="card__swoosh" viewBox="0 0 660 377" preserveAspectRatio="none" aria-hidden="true">
    <path fill="var(--leaf)" d="M0,312 C210,322 430,250 610,200 C430,272 210,352 0,356 Z"/>
    <path fill="var(--charcoal-deep)" d="M0,377 L0,360 C220,350 430,262 660,150 L660,377 Z"/>
  </svg>

  <h2 class="holder-name">Tobias Verhoek</h2>

  <div class="brand-mark">
    <span class="brand-mark__dot"></span>
    <p class="brand-mark__name">Bright Meadow<br>Lawn &amp; Landscape</p>
  </div>

  <ul class="contact-list">
    <li>
      <svg viewBox="0 0 24 24"><path d="M6.6 10.8a15.1 15.1 0 0 0 6.6 6.6l2.2-2.2c.3-.3.7-.4 1-.2 1.1.4 2.3.6 3.6.6.6 0 1 .4 1 1V20c0 .6-.4 1-1 1C10.6 21 3 13.4 3 4c0-.6.4-1 1-1h3.5c.6 0 1 .4 1 1 0 1.3.2 2.5.6 3.6.1.3 0 .7-.2 1z"/></svg>
      410-555-2916
    </li>
    <li>
      <svg viewBox="0 0 24 24"><path d="M2 5h20v14H2z M4 7v.4l8 5 8-5V7l-8 5z" fill-rule="evenodd"/></svg>
      Tverhoek27@mailbrook.net
    </li>
  </ul>

  <p class="insured">Fully Insured</p>
</section>

</body>
</html>
```